University Student Business Card

Looking for a professional university student business card. Student is studying business with a focus on marketing. Some combination using a monogram and/or full name on the front with full name, university details and contact information on the back. Card should be modern design for a young professional. Prefer use of royal blue, black and white but am open to other uses of colour palette if it reinforces young/trendy style. Initials for a monogram are: KM. Full details will be provided in private consultation with designer(s).

Target Market(s)

Professional business people, marketers, advertisers, consultants

Industry/Entity Type

Business, marketing

Contact Information for Business Card

Monogram or personal logo, full name, university name, program of study, phone number, email address, linkedin address

Font styles to use
Other font styles liked:
• Open to suggestion to fulfill above requirements

Colors
0054AA
0677BA
7BADD7
CADEEF
E8F1F8

Requirements
Must have
• Monogram using letters K and M, and incorporate the business card details listed in the brief (specific details including personal contact info will be shared with successful designer to ensure privacy)
Nice to have
• Personal brand using monogram or personal logo (not a business logo)

```html
<!DOCTYPE html>
<html lang="en">
<head>
<meta charset="utf-8">
<title>Kara Morgan – Student Business Card</title>
<link rel="stylesheet" href="https://fonts.googleapis.com/css2?family=Montserrat:wght@500;600;700&family=Arimo:wght@400&display=swap">
<style>
  :root {
    --backdrop: #0b0b0c;
    --card: #2a2b2e;
    --card-shade: #25262a;
    --rule: #45474c;
    --royal: #0054aa;
    --royal-bright: #0677ba;
    --text-light: #ffffff;
    --mark-dark: #3a3c40;
  }
  * { margin: 0; padding: 0; box-sizing: border-box; }
  html, body {
    width: 1200px; height: 820px; overflow: hidden;
    background: radial-gradient(ellipse at 50% 40%, #1d1e20 0%, var(--backdrop) 75%);
  }
  .canvas {
    position: relative; width: 1200px; height: 820px;
    display: flex; align-items: center; justify-content: center; gap: 50px;
  }
  .card {
    position: relative; width: 540px; height: 310px;
    background: linear-gradient(135deg, var(--card) 0%, var(--card-shade) 100%);
    border-bottom: 4px solid var(--royal);
    border-left: 2px solid var(--royal);
    box-shadow: 0 18px 40px rgba(0,0,0,.6);
    font-family: "Arimo", Arial, sans-serif;
    color: var(--text-light);
    overflow: hidden;
  }
  .monogram {
    position: absolute; top: 34px; right: 44px;
    font-family: "Montserrat", sans-serif; font-weight: 700;
    font-size: 96px; letter-spacing: 2px; line-height: 1;
  }
  .monogram--blue { color: var(--royal); }
  .monogram--tonal { color: var(--mark-dark); }
  .rule {
    position: absolute; left: 44px; right: 44px; height: 1px;
    background: var(--rule);
  }
  /* contact side */
  .contact .rule { top: 176px; }
  .university {
    position: absolute; left: 44px; top: 140px;
    font-family: "Montserrat", sans-serif; font-weight: 600;
    font-size: 26px; color: var(--royal); letter-spacing: .5px;
  }
  .contact-list {
    position: absolute; left: 44px; top: 196px; list-style: none;
    font-size: 16px; line-height: 26px;
  }
  .contact-list li { display: flex; align-items: center; gap: 10px; }
  .contact-list svg { width: 15px; height: 15px; fill: var(--royal-bright); }
  .address {
    position: absolute; right: 44px; top: 200px; text-align: right;
    font-size: 16px; line-height: 22px;
  }
  /* name side */
  .name-side .rule { top: 160px; }
  .person {
    position: absolute; left: 44px; top: 206px;
  }
  .person__name {
    font-family: "Montserrat", sans-serif; font-weight: 600;
    font-size: 24px; color: var(--royal); letter-spacing: .5px;
  }
  .person__role { font-size: 16px; margin-top: 4px; }
  .profile-link {
    position: absolute; right: 44px; top: 214px;
    display: flex; align-items: center; gap: 8px; font-size: 14px;
  }
  .profile-link__dot {
    width: 20px; height: 20px; border-radius: 50%; background: var(--royal-bright);
  }
</style>
</head>
<body>
<main class="canvas">
  <section class="card contact" aria-label="Card back with contact details">
    <div class="monogram monogram--blue">KM</div>
    <h2 class="university">UNIVERSITY NAME</h2>
    <div class="rule"></div>
    <ul class="contact-list">
      <li><svg viewBox="0 0 24 24" aria-hidden="true"><path d="M6.6 10.8a15 15 0 0 0 6.6 6.6l2.2-2.2c.3-.3.7-.4 1-.2 1.1.4 2.3.6 3.6.6.6 0 1 .4 1 1V20c0 .6-.4 1-1 1A17 17 0 0 1 3 4c0-.6.4-1 1-1h3.5c.6 0 1 .4 1 1 0 1.3.2 2.5.6 3.6.1.3 0 .7-.2 1z"/></svg>044-555 010 234</li>
      <li><svg viewBox="0 0 24 24" aria-hidden="true"><path d="M2 5h20v14H2zm2 2v.5l8 5 8-5V7zm0 3v7h16v-7l-8 5z"/></svg>hello@kmstudio.net</li>
      <li><svg viewBox="0 0 24 24" aria-hidden="true"><path d="M12 2a10 10 0 1 0 0 20 10 10 0 0 0 0-20zm6.9 9h-3a15 15 0 0 0-1.3-5.6A8 8 0 0 1 18.9 11zM12 4.1c.9 1.3 1.7 3.7 1.9 6.9h-3.8c.2-3.2 1-5.6 1.9-6.9zM9.4 5.4A15 15 0 0 0 8.1 11h-3a8 8 0 0 1 4.3-5.6zM5.1 13h3a15 15 0 0 0 1.3 5.6A8 8 0 0 1 5.1 13zm6.9 6.9c-.9-1.3-1.7-3.7-1.9-6.9h3.8c-.2 3.2-1 5.6-1.9 6.9zm2.6-1.3a15 15 0 0 0 1.3-5.6h3a8 8 0 0 1-4.3 5.6z"/></svg>www.kmportfolio.net</li>
    </ul>
    <p class="address">18 Harbour Lane, Suite 4<br>20931, Northland</p>
  </section>

  <section class="card name-side" aria-label="Card front with name">
    <div class="monogram monogram--tonal">KM</div>
    <div class="rule"></div>
    <div class="person">
      <h1 class="person__name">KARA MORGAN</h1>
      <p class="person__role">Business Marketing</p>
    </div>
    <p class="profile-link"><span class="profile-link__dot"></span>profile.kmlink.net</p>
  </section>
</main>
</body>
</html>
```